Classic Car Web Banner Set Design

We need a set of banner ads designed for a manufacturing and retail company that sells weatherstripping for classic American vehicles (muscle cars, antique cars, classic cars). The banner ad must include our logo. There should be at least one car in the graphic, whole or partial. Our primary colors are Red and Black. Either a representation of auto weatherstripping or the words "Quality Weatherstripping" should be in the design.

Company name is "Harlow Gasket Works"

Sizes Needed: 300x250, 300x100, 728x90, 160x600, 120x90, 728x90, 234x60, 320x100, 750x100, 250x250

Target Market(s)

Consumer Audience, Classic Car Market

Industry/Entity Type

Retail

Font styles to use
Sans Serif

Colors
ec1f27

Requirements
Must have
• Red and Black primary colors. Company logo. Graphically show weatherstripping and/or automotive icons. If a vehicle is used, it must be an American vehicle.
Nice to have
• PSD files for selected entry.
Should not have
• no people

```html
<!DOCTYPE html>
<html lang="en">
<head>
<meta charset="utf-8">
<title>Harlow Gasket Works – Quality Weatherstripping Banner</title>
<link rel="stylesheet" href="https://fonts.googleapis.com/css2?family=Oswald:wght@600;700&family=Archivo+Narrow:ital,wght@0,700;1,700&display=swap">
<style>
  :root {
    --brand-red: #ec1f27;
    --brand-red-dark: #b3151b;
    --ink: #111111;
    --ink-soft: #2a2a2a;
    --white: #ffffff;
    --photo-light: #e4e4e4;
    --photo-mid: #9a9a9a;
    --photo-dark: #3c3c3c;
  }
  * { box-sizing: border-box; margin: 0; padding: 0; }
  html, body {
    width: 1200px; height: 1000px; overflow: hidden;
    background: var(--white);
  }
  .banner {
    position: relative; width: 1200px; height: 1000px; overflow: hidden;
    background: var(--white);
  }
  .car-photo {
    position: absolute; inset: 0;
    background:
      radial-gradient(ellipse 60% 40% at 15% 95%, var(--photo-light), transparent 70%),
      radial-gradient(ellipse 70% 45% at 75% 78%, var(--photo-dark), transparent 75%),
      linear-gradient(180deg, var(--photo-mid) 0%, #c9c9c9 35%, var(--photo-mid) 65%, #6e6e6e 100%);
  }
  .header-band {
    position: absolute; left: 0; top: 0; width: 1200px; height: 248px;
    background: var(--ink);
    border-bottom: 10px solid var(--brand-red);
    display: flex; flex-direction: column; align-items: center; justify-content: center;
  }
  .headline {
    font-family: "Oswald", sans-serif;
    color: var(--white);
    font-weight: 700;
    text-transform: uppercase;
    letter-spacing: 8px;
    line-height: 1.08;
    text-align: center;
    font-size: 84px;
  }
  .flags {
    position: absolute; left: 0; top: 258px; width: 1200px; height: 260px;
  }
  .samples {
    position: absolute; left: 0; top: 540px; width: 1200px; height: 260px;
  }
  .logo-box {
    position: absolute; left: 8px; top: 852px; width: 252px; height: 140px;
    background: var(--ink);
    border: 5px solid var(--white);
    outline: 3px solid var(--ink);
    display: flex; align-items: center; justify-content: center;
    padding: 8px;
  }
  .logo-name {
    font-family: "Archivo Narrow", sans-serif;
    font-weight: 700;
    color: var(--white);
    font-size: 36px;
    line-height: 1.05;
    text-align: center;
  }
  .contact {
    position: absolute; left: 282px; top: 868px;
    font-family: "Archivo Narrow", sans-serif;
  }
  .contact-phone {
    color: var(--ink);
    font-size: 82px; font-weight: 700; line-height: 1; letter-spacing: 1px;
  }
  .contact-web {
    color: var(--brand-red-dark);
    font-size: 30px; font-weight: 700; font-style: italic; line-height: 1.2;
  }
</style>
</head>
<body>
<div class="banner">
  <div class="car-photo" role="img" aria-label="Black and white photograph of a classic American car front grille and headlights"></div>

  <header class="header-band">
    <h1 class="headline">Quality<br>Weatherstripping</h1>
  </header>

  <svg class="flags" viewBox="0 0 1200 260" aria-hidden="true">
    <path d="M66 10 H242 V250 L154 200 L66 250 Z" fill="var(--brand-red)"/>
    <path d="M348 10 H564 V220 Q512 160 456 200 Q400 250 348 220 Z" fill="var(--ink-soft)"/>
    <path d="M628 10 H804 V180 Q804 250 716 250 Q628 250 628 180 Z" fill="var(--brand-red)"/>
    <path d="M908 10 H1124 V180 L1016 260 L908 180 Z" fill="var(--ink-soft)"/>
  </svg>

  <svg class="samples" viewBox="0 0 1200 260" aria-hidden="true">
    <defs>
      <radialGradient id="sampleTone" cx="50%" cy="50%" r="50%">
        <stop offset="0%" stop-color="#1a1a1a"/>
        <stop offset="60%" stop-color="#3a3a3a"/>
        <stop offset="100%" stop-color="#f2f2f2"/>
      </radialGradient>
    </defs>
    <g>
      <circle cx="156" cy="128" r="122" fill="var(--white)"/>
      <circle cx="156" cy="128" r="96" fill="url(#sampleTone)" role="img" aria-label="Rubber weatherstrip sample"/>
      <circle cx="452" cy="128" r="122" fill="var(--white)"/>
      <circle cx="452" cy="128" r="96" fill="url(#sampleTone)" role="img" aria-label="Rubber door seal profile"/>
      <circle cx="748" cy="128" r="122" fill="var(--white)"/>
      <circle cx="748" cy="128" r="96" fill="url(#sampleTone)" role="img" aria-label="Rubber bulb seal profile"/>
      <circle cx="1040" cy="128" r="122" fill="var(--white)"/>
      <circle cx="1040" cy="128" r="96" fill="url(#sampleTone)" role="img" aria-label="Coiled rubber trunk seal"/>
    </g>
  </svg>

  <div class="logo-box">
    <span class="logo-name">Harlow<br>Gasket Works</span>
  </div>

  <div class="contact">
    <p class="contact-phone">800-555-0172</p>
    <p class="contact-web">www.harlowgasket.com</p>
  </div>
</div>
</body>
</html>
```